Consulting Company needs business card design

We need a business card design for a new consulting and business solutions company based in Bermuda called Corvale Partners Limited. Looking for a double sided business card with one side only including the company logo thats attached and the other including contact information. Logo contains blue and turquoise colors and is fine to be on both sides of the card.
Contact Information for Business Card
Corvale Partners Limited
P.O. Box HM318
Devonshire DV BX
Bermuda
Name: Marcus Pellegrin
Position: Director
Telephone: 1 441 733 4906
Email: mpellegrin@corvale.example
Website: www.corvale.example

```html
<!DOCTYPE html>
<html lang="en">
<head>
<meta charset="utf-8">
<title>Corvale Partners Limited – Business Card</title>
<link href="https://fonts.googleapis.com/css2?family=Roboto:wght@300;500&family=Roboto+Condensed:wght@400&display=swap" rel="stylesheet">
<style>
  :root {
    --stage: #2a2d31;
    --paper: #ffffff;
    --sky: #29a3df;
    --teal: #10b7bd;
    --slate: #3d4654;
    --ink: #1d1f22;
    --edge: rgba(0,0,0,.35);
  }
  * { margin: 0; padding: 0; box-sizing: border-box; }
  html, body { width: 1200px; height: 900px; overflow: hidden; background: var(--stage); }
  .stage {
    width: 1200px; height: 900px;
    display: flex; flex-direction: column; align-items: center; justify-content: center; gap: 40px;
  }
  .card {
    position: relative; width: 700px; height: 400px;
    background: var(--paper); border-radius: 28px; overflow: hidden;
    box-shadow: 0 10px 30px var(--edge);
  }
  .card-art { position: absolute; inset: 0; }
  .name {
    position: absolute; left: 40px; top: 26px;
    font-family: "Roboto", sans-serif; font-weight: 300; font-size: 40px; letter-spacing: .5px;
    color: var(--ink); text-transform: uppercase;
  }
  .name .surname { color: var(--sky); }
  .role {
    position: absolute; left: 340px; top: 78px;
    font-family: "Roboto Condensed", sans-serif; font-size: 15px; color: var(--ink); text-transform: uppercase;
  }
  .contact {
    position: absolute; right: 70px;
    font-family: "Roboto Condensed", sans-serif; font-size: 19px; text-transform: uppercase; text-align: right;
  }
  .contact.phone { top: 212px; color: #ffffff; }
  .contact.email { top: 262px; color: #ffffff; text-transform: uppercase; }
  .contact.address { top: 310px; color: var(--ink); font-size: 17px; line-height: 21px; }
  .website {
    position: absolute; left: 70px; top: 262px;
    font-family: "Roboto Condensed", sans-serif; font-size: 16px; color: var(--ink); text-transform: uppercase;
  }
  .logo-side { display: flex; align-items: center; justify-content: center; gap: 16px; }
  .logo-dot { width: 54px; height: 54px; border-radius: 50%; background: var(--teal); }
  .logo-name {
    font-family: "Roboto", sans-serif; font-weight: 500; font-size: 34px; color: var(--sky);
    text-transform: uppercase; letter-spacing: 1px;
  }
</style>
</head>
<body>
<main class="stage">
  <section class="card contact-side">
    <svg class="card-art" width="700" height="400" viewBox="0 0 700 400">
      <!-- colour bands -->
      <rect class="band-teal" x="250" y="168" width="450" height="132" fill="var(--teal)"/>
      <rect class="band-slate" x="300" y="200" width="400" height="52" fill="var(--slate)"/>
      <path class="band-sky" d="M0 96 H300 A110 110 0 0 1 300 240 H150 L0 232 Z" fill="var(--sky)"/>
      <rect class="tab-web" x="0" y="250" width="52" height="40" fill="var(--sky)"/>
      <rect class="tab-pin" x="660" y="300" width="40" height="44" fill="var(--teal)"/>
      <!-- icons -->
      <g class="icon-web">
        <circle cx="36" cy="270" r="13" fill="var(--sky)" stroke="#fff" stroke-width="1.5"/>
        <circle cx="36" cy="270" r="7" fill="none" stroke="#fff" stroke-width="1.3"/>
        <path d="M29 270 H43 M36 263 V277" stroke="#fff" stroke-width="1.2"/>
      </g>
      <g class="icon-phone">
        <circle cx="660" cy="226" r="14" fill="var(--sky)"/>
        <path d="M654 220 q2 -3 4 0 l1 3 -2 2 q2 4 5 5 l2 -2 3 1 q3 2 0 4 q-10 2 -13 -13z" fill="#fff"/>
      </g>
      <g class="icon-mail">
        <circle cx="660" cy="276" r="14" fill="var(--sky)"/>
        <rect x="652" y="270" width="16" height="11" rx="1.5" fill="none" stroke="#fff" stroke-width="1.5"/>
        <path d="M652 271 L660 277 L668 271" fill="none" stroke="#fff" stroke-width="1.5"/>
      </g>
      <g class="icon-pin">
        <circle cx="675" cy="322" r="13" fill="var(--sky)"/>
        <path d="M675 330 C669 323 669 320 669 318 a6 6 0 0 1 12 0 c0 2 0 5 -6 12z" fill="none" stroke="#fff" stroke-width="1.5"/>
        <circle cx="675" cy="318" r="2" fill="#fff"/>
      </g>
    </svg>
    <h1 class="name">Marcus <span class="surname">Pellegrin</span></h1>
    <p class="role">Director</p>
    <p class="website">www.corvale.example</p>
    <p class="contact phone">1 441 733 4906</p>
    <p class="contact email">mpellegrin@corvale.example</p>
    <p class="contact address">Corvale Partners Limited<br>P.O. Box HM318 Devonshire DV BX<br>Bermuda</p>
  </section>

  <section class="card logo-side">
    <span class="logo-dot"></span>
    <span class="logo-name">Corvale Partners Limited</span>
  </section>
</main>
</body>
</html>
```